Business Card Design - Furniture Retail

Open to both Single or double sided design

We are launching a online ecommerce store that sells Scandinavian/Danish style of furniture in Australia.

We aspire to provide stylish but classic and designers' selection of furniture to the Australia public at affordable price. For the style of the furniture we are selling, please see the following links:

https://www.filecrate.example/sh/qk3mzr8wlp/BXTpLnR4vQ7cYdHs?dl=0

The style of the design we are looking for is clean, simple that look Scandinavian/Danish but yet it is timeless classic.

Aspiring Design
http://www.lindmora.com
http://tobyquell.com.au/
http://vekt.furniture/
http://www.olvo.com/
Updates

Please display the card on normal angle for both front and back instead of funny angle. Please keep it display when displaying the design of the business cards so that we can focus on the designs rather than being confused by the unnecessary stuffs like the hands or background

I think there is already enough curve line on the logo itself so anything extra of the curve on the business card would be really unnecessary. Please avoid using any of the extra curve line on the business card, other than the logo itself. Thanks

Regular card and give them a matt celloglaze to create texture on card that makes it looked luxury and expensive.

Please display design on normal angle! Please only use white colour in the background (not the business card but the referring to the submission) rather than anything fancy so that we can focus on the design.

Target Market(s)

High end market consumers who are financially capable and who has good taste and appreciate good design

aged between 28 - 45 white collars professional/businessmen who live in metropolitan areas

Industry/Entity Type

Business

Font styles to use
Serif
Sans Serif

Requirements
Must have
• Regular card and give them a matt celloglaze to create texture on card that makes it looked luxury and expensive.

Please use the logo from the uploaded files

Company Name: Milo Verhagen
Name: Milo Reeb
Phone: +614 27 305 641
Website: www.miloverhagen.com.au
Email: milo@miloverhagen.com.au
Nice to have
• Colour is not limited to black and white
Should not have
• The concept photos of the furniture should NOT be used in the FRONT page of the business card.

```html
<!DOCTYPE html>
<html lang="en">
<head>
<meta charset="utf-8">
<title>Milo Verhagen — Business Cards</title>
<link rel="stylesheet" href="https://fonts.googleapis.com/css2?family=Lora:wght@400&family=Italianno&display=swap">
<style>
  :root {
    --page: #ffffff;
    --card-light: #eef0ef;
    --card-light-edge: #f6f7f6;
    --card-dark: #000000;
    --ink: #141414;
    --ink-light: #f2f2f2;
    --gold: #8c6422;
    --gold-soft: #9a7430;
  }
  * { box-sizing: border-box; margin: 0; padding: 0; }
  html, body {
    width: 1200px;
    height: 835px;
    overflow: hidden;
    background: var(--page);
  }
  .sheet {
    position: relative;
    width: 1200px;
    height: 835px;
    font-family: "Lora", Georgia, serif;
  }
  .card {
    position: absolute;
    width: 512px;
    height: 332px;
    overflow: hidden;
  }
  .card--light {
    background: linear-gradient(135deg, var(--card-light-edge) 0%, var(--card-light) 100%);
    color: var(--ink);
    box-shadow: 0 0 0 1px #e2e4e3;
  }
  .card--dark {
    background: var(--card-dark);
    color: var(--ink-light);
  }
  .card--front-top { left: 70px;  top: 30px; }
  .card--back-top  { left: 638px; top: 32px; }
  .card--front-bottom { left: 70px;  top: 452px; }
  .card--back-bottom  { left: 634px; top: 454px; }

  .wordmark {
    font-family: "Lora", Georgia, serif;
    font-weight: 400;
    text-transform: uppercase;
    white-space: nowrap;
  }
  .card__wordmark {
    position: absolute;
    right: 26px;
    top: 40px;
    font-size: 26px;
    letter-spacing: 0.5px;
  }
  .card__name {
    position: absolute;
    left: 22px;
    top: 156px;
    font-size: 29px;
    color: var(--gold);
    letter-spacing: 0.5px;
  }
  .card__contact {
    position: absolute;
    left: 17px;
    top: 229px;
    list-style: none;
    font-size: 16px;
    line-height: 22px;
  }
  .card__contact .label--spaced { letter-spacing: 1.5px; }

  .card__lockup {
    position: absolute;
    left: 0;
    right: 0;
    top: 120px;
    text-align: center;
  }
  .card__lockup .wordmark {
    font-size: 46px;
    letter-spacing: 1px;
  }
  .card__tagline {
    margin-top: 18px;
    font-family: "Italianno", cursive;
    font-size: 30px;
    color: var(--gold-soft);
    letter-spacing: 0.5px;
  }
</style>
</head>
<body>
<main class="sheet">

  <section class="card card--light card--front-top" aria-label="Card front, light">
    <div class="card__wordmark wordmark">Milo Verhagen</div>
    <div class="card__name">Milo Reeb</div>
    <ul class="card__contact">
      <li>phone: +614 27 305 641</li>
      <li>website: www.miloverhagen.com.au</li>
      <li><span class="label--spaced">email:</span> milo@miloverhagen.com.au</li>
    </ul>
  </section>

  <section class="card card--light card--back-top" aria-label="Card back, light">
    <div class="card__lockup">
      <div class="wordmark">Milo Verhagen</div>
      <div class="card__tagline">Scandinavia style of furniture</div>
    </div>
  </section>

  <section class="card card--dark card--front-bottom" aria-label="Card front, dark">
    <div class="card__wordmark wordmark">Milo Verhagen</div>
    <div class="card__name">Milo Reeb</div>
    <ul class="card__contact">
      <li>phone: +614 27 305 641</li>
      <li>website: www.miloverhagen.com.au</li>
      <li><span class="label--spaced">email:</span> milo@miloverhagen.com.au</li>
    </ul>
  </section>

  <section class="card card--dark card--back-bottom" aria-label="Card back, dark">
    <div class="card__lockup">
      <div class="wordmark">Milo Verhagen</div>
      <div class="card__tagline">Scandinavia style of furniture</div>
    </div>
  </section>

</main>
</body>
</html>
```